label design for soy candle

I am a start up making soy candles and other products involving scents.
On the label should be in writing : the scent, Handgemacht in der Schweiz, Sojakerze, my logo with the name Pertwick Candles on it. I will upload the currant label of my candles, but I want something more fashioned. The color of the label should be black with the scent written in gold, and the rest in white. Or maybe suggest something different, I am open to new designs. I am also open to change the logo, except the flower has to stay.
Sizes : square 60x60mm / round 50mm / rectangle 70x20mm ( for different jars )

```html
<!DOCTYPE html>
<html lang="de">
<head>
<meta charset="utf-8">
<title>Pertwick Candles – Etikett Sojakerze</title>
<link rel="stylesheet" href="https://fonts.googleapis.com/css2?family=Oswald:wght@400;500;600&display=swap">
<style>
  :root {
    --backdrop: #e9e9e9;
    --label-paper: #f7f7f7;
    --ornament-tone: #e6e6e6;
    --frame-line: #6d6d6d;
    --rule-line: #8f8f8f;
    --scent-gold: #b3951f;
    --ink: #151515;
  }
  * { margin: 0; padding: 0; box-sizing: border-box; }
  html, body {
    width: 1200px;
    height: 1200px;
    overflow: hidden;
    background: var(--backdrop);
  }
  .canvas {
    position: relative;
    width: 1200px;
    height: 1200px;
    background: var(--backdrop);
  }
  .label {
    position: absolute;
    left: 200px;
    top: 200px;
    width: 800px;
    height: 800px;
    background: var(--label-paper);
    box-shadow: 0 2px 14px rgba(0,0,0,0.06);
    overflow: hidden;
  }
  .corner-ornament {
    position: absolute;
  }
  .corner-ornament.top-left {
    left: 0; top: 0; width: 240px; height: 130px;
    background: linear-gradient(135deg, var(--ornament-tone), var(--label-paper));
  }
  .corner-ornament.top-right {
    right: 0; top: 0; width: 170px; height: 290px;
    background: linear-gradient(225deg, var(--ornament-tone), var(--label-paper));
  }
  .corner-ornament.bottom-left {
    left: 0; bottom: 0; width: 130px; height: 420px;
    background: linear-gradient(45deg, var(--ornament-tone), var(--label-paper));
  }
  .corner-ornament.bottom-right {
    right: 0; bottom: 0; width: 170px; height: 280px;
    background: linear-gradient(315deg, var(--ornament-tone), var(--label-paper));
  }
  .label-lines {
    position: absolute;
    inset: 0;
    width: 800px;
    height: 800px;
  }
  .label-lines .frame { fill: none; stroke: var(--frame-line); stroke-width: 1.6; }
  .label-lines .rule { stroke: var(--rule-line); stroke-width: 1.6; }
  .scent-name {
    position: absolute;
    top: 140px;
    left: 0;
    width: 100%;
    text-align: center;
    font-family: 'Oswald', sans-serif;
    font-weight: 500;
    font-size: 34px;
    letter-spacing: 2px;
    color: var(--scent-gold);
  }
  .brand {
    position: absolute;
    top: 370px;
    left: 0;
    width: 100%;
    display: flex;
    align-items: center;
    justify-content: center;
    gap: 14px;
  }
  .brand-dot {
    width: 22px;
    height: 22px;
    border-radius: 50%;
    background: var(--ink);
  }
  .brand-name {
    font-family: 'Oswald', sans-serif;
    font-weight: 500;
    font-size: 30px;
    letter-spacing: 1px;
    color: var(--ink);
  }
  .product-info {
    position: absolute;
    top: 630px;
    left: 0;
    width: 100%;
    text-align: center;
    font-family: 'Oswald', sans-serif;
    font-weight: 600;
    font-size: 22px;
    letter-spacing: 1.5px;
    color: var(--ink);
  }
</style>
</head>
<body>
<main class="canvas">
  <section class="label">
    <div class="corner-ornament top-left" role="img" aria-label="Fine curved line ornament, top left corner"></div>
    <div class="corner-ornament top-right" role="img" aria-label="Fine curved line ornament, top right corner"></div>
    <div class="corner-ornament bottom-left" role="img" aria-label="Fine curved line ornament, bottom left corner"></div>
    <div class="corner-ornament bottom-right" role="img" aria-label="Fine curved line ornament, bottom right corner"></div>

    <svg class="label-lines" viewBox="0 0 800 800" aria-hidden="true">
      <rect class="frame" x="40" y="40" width="720" height="720"/>
      <line class="rule" x1="180" y1="245" x2="620" y2="245"/>
      <line class="rule" x1="180" y1="535" x2="620" y2="535"/>
    </svg>

    <h1 class="scent-name">THE SCENT</h1>

    <div class="brand">
      <span class="brand-dot"></span>
      <span class="brand-name">PERTWICK CANDLES</span>
    </div>

    <p class="product-info">HANDGEMACHT IN DER SCHWEIZ, SOJAKERZE</p>
  </section>
</main>
</body>
</html>
```